Lumen Tide flyer KQ Dive Bonaire

On Bonaire we are working on a Lumen Tide project. Growing corals and placing them on the reef, to keep the reefs healthy. KQ Dive has her own coral tree. We are giving Lumen Tide courses, so people can help us to protect the reef.
We like to have a flyer to sell these courses to our guests.
It needs to be informative and appealing for divers to participate.

Target Market(s)

Divers

Industry/Entity Type

Diving / tourism industry

Font styles to use
Sans Serif

Colors
0054AA
0677BA
7BADD7
CADEEF
E8F1F8
F0912C
F2A743
F7CA91
FBE8D2
FDF5EE

Requirements
Must have
• The pictures we added as attachment
Should not have
• No pictures not from Bonaire

```html
<!DOCTYPE html>
<html lang="en">
<head>
<meta charset="utf-8">
<title>Lumen Tide flyers – KQ Dive Bonaire</title>
<link href="https://fonts.googleapis.com/css2?family=Montserrat:wght@700;800&family=Lato:wght@400;700&display=swap" rel="stylesheet">
<style>
  :root {
    --blue-deep: #0054AA;
    --blue: #0677BA;
    --blue-soft: #7BADD7;
    --blue-pale: #CADEEF;
    --blue-mist: #E8F1F8;
    --orange: #F0912C;
    --orange-warm: #F2A743;
    --orange-soft: #F7CA91;
    --paper: #FDF5EE;
    --navy: #1F2F5E;
    --sea-dark: #0B2F7A;
    --sea-night: #0A2466;
    --sand: #C9A77A;
    --coral: #9C7246;
  }
  * { box-sizing: border-box; margin: 0; padding: 0; }
  html, body { width: 1025px; height: 1200px; overflow: hidden; }
  body {
    background: var(--blue-mist);
    font-family: "Lato", sans-serif;
    display: flex;
    align-items: center;
    justify-content: center;
    gap: 35px;
  }
  .flyer {
    position: relative;
    width: 470px;
    height: 663px;
    background: var(--paper);
    overflow: hidden;
    box-shadow: 0 10px 30px rgba(0, 40, 100, .18);
  }
  .partner-row {
    position: absolute;
    top: 28px; left: 34px;
    display: flex; align-items: center; gap: 12px;
    z-index: 3;
  }
  .partner-badge { width: 30px; height: 30px; border-radius: 50%; background: var(--blue); }
  .partner-badge.square { width: 62px; height: 24px; border-radius: 3px; background: var(--sea-dark); }
  .brand {
    position: absolute;
    top: 30px; right: 30px;
    display: flex; align-items: center; gap: 8px;
    font-family: "Montserrat", sans-serif;
    font-weight: 800; font-size: 20px;
    color: var(--blue-deep);
    z-index: 3;
  }
  .brand-dot { width: 26px; height: 26px; border-radius: 50%; background: var(--orange-warm); }
  .title {
    position: absolute;
    font-family: "Montserrat", sans-serif;
    font-weight: 800;
    font-size: 31px;
    line-height: 1.3;
    text-transform: uppercase;
    color: var(--blue-deep);
    z-index: 3;
  }
  .title .light { color: var(--blue-soft); }
  .title .mid { color: var(--blue); }

  .photo { position: absolute; left: 0; right: 0; }
  .photo-edge { position: absolute; left: 0; top: -1px; width: 100%; height: 70px; display: block; }

  /* Specialty flyer */
  .specialty .title { top: 108px; left: 34px; }
  .benefits {
    position: absolute; top: 262px; left: 34px; right: 26px;
    display: flex; justify-content: space-between; list-style: none;
    z-index: 3;
  }
  .benefits li {
    display: flex; gap: 8px; width: 130px;
    font-size: 11px; line-height: 1.35; color: #3a4660;
  }
  .tick { flex: none; width: 17px; height: 17px; }
  .specialty .photo {
    top: 318px; bottom: 0;
    background:
      radial-gradient(ellipse 40% 30% at 30% 58%, rgba(242,167,67,.55), rgba(242,167,67,0) 70%),
      radial-gradient(ellipse 30% 22% at 62% 60%, rgba(202,222,239,.55), rgba(202,222,239,0) 70%),
      radial-gradient(ellipse 70% 18% at 50% 100%, rgba(202,222,239,.9), rgba(202,222,239,0) 75%),
      linear-gradient(180deg, var(--blue-soft) 0%, var(--blue) 22%, var(--blue-deep) 48%, var(--sea-night) 72%, #2D5FA5 90%, #7FA8D2 100%);
  }

  /* Discover flyer */
  .discover .title { top: 112px; left: 0; right: 0; text-align: center; }
  .intro {
    position: absolute; top: 208px; left: 50px; right: 50px;
    text-align: center; font-size: 11px; line-height: 1.45; color: #2c3550;
    z-index: 3;
  }
  .discover .photo-main {
    top: 258px; height: 278px;
    background:
      radial-gradient(ellipse 30% 18% at 40% 38%, rgba(122,40,50,.45), rgba(122,40,50,0) 70%),
      radial-gradient(ellipse 60% 30% at 35% 82%, rgba(156,114,70,.9), rgba(156,114,70,0) 75%),
      radial-gradient(ellipse 50% 28% at 75% 75%, rgba(201,167,122,.9), rgba(201,167,122,0) 75%),
      linear-gradient(180deg, var(--blue-pale) 0%, #8E9CCB 28%, #6E6FA8 50%, #8A6E52 72%, var(--sand) 100%);
  }
  .photo-pair { position: absolute; left: 0; right: 0; top: 536px; height: 98px; display: flex; gap: 2px; }
  .photo-pair div { flex: 1; }
  .photo-pair .shallows {
    background:
      radial-gradient(ellipse 45% 35% at 40% 70%, rgba(200,140,70,.85), rgba(200,140,70,0) 70%),
      linear-gradient(180deg, #3E8FAE 0%, #7DB3C4 40%, #D8C4A2 100%);
  }
  .photo-pair .field {
    background:
      radial-gradient(ellipse 60% 45% at 60% 75%, rgba(176,150,110,.9), rgba(176,150,110,0) 75%),
      linear-gradient(180deg, #1F5F86 0%, #3E7C96 45%, #9E8A6A 100%);
  }

  .social {
    position: absolute; left: 0; right: 0; bottom: 0; height: 29px;
    display: flex; align-items: center; justify-content: center; gap: 6px;
    font-size: 10px; font-weight: 700; color: #fff;
    z-index: 3;
  }
  .social-mark { width: 10px; height: 10px; background: #fff; border-radius: 2px; }
  .discover .social { background: var(--navy); }
  .specialty .social { bottom: 14px; }
</style>
</head>
<body>

<article class="flyer specialty">
  <div class="partner-row">
    <span class="partner-badge"></span>
    <span class="partner-badge square"></span>
  </div>
  <div class="brand"><span class="brand-dot"></span>KQ Dive</div>
  <h1 class="title">
    <span class="light">Lumen Tide</span><br>
    <span class="mid">Diver Distinctive</span><br>
    Specialty
  </h1>
  <ul class="benefits">
    <li><svg class="tick" viewBox="0 0 18 18"><circle cx="9" cy="9" r="8" fill="none" stroke="var(--orange)" stroke-width="1.5"/><path d="M5.5 9.2l2.4 2.4 4.6-4.8" fill="none" stroke="var(--orange)" stroke-width="1.5"/></svg>Help restore our reefs!</li>
    <li><svg class="tick" viewBox="0 0 18 18"><circle cx="9" cy="9" r="8" fill="none" stroke="var(--orange)" stroke-width="1.5"/><path d="M5.5 9.2l2.4 2.4 4.6-4.8" fill="none" stroke="var(--orange)" stroke-width="1.5"/></svg>Become an active member in helping restore our reef.</li>
    <li><svg class="tick" viewBox="0 0 18 18"><circle cx="9" cy="9" r="8" fill="none" stroke="var(--orange)" stroke-width="1.5"/><path d="M5.5 9.2l2.4 2.4 4.6-4.8" fill="none" stroke="var(--orange)" stroke-width="1.5"/></svg>In 2 days and 3 dives you learn all about the reef of Bonaire.</li>
  </ul>
  <div class="photo" role="img" aria-label="Underwater photo of a diver tending a coral tree on a Bonaire reef, a second diver behind">
    <svg class="photo-edge" viewBox="0 0 470 70" preserveAspectRatio="none" aria-hidden="true">
      <path d="M0 0H470V40C440 58 410 30 380 44C350 60 320 34 290 46C260 60 230 36 200 48C170 62 140 38 110 50C80 62 50 40 24 52C14 56 6 54 0 50Z" fill="var(--paper)"/>
    </svg>
  </div>
  <div class="social"><span class="social-mark"></span><span class="social-mark"></span>kqdivebonaire</div>
</article>

<article class="flyer discover">
  <div class="partner-row">
    <span class="partner-badge"></span>
    <span class="partner-badge square"></span>
  </div>
  <div class="brand"><span class="brand-dot"></span>KQ Dive</div>
  <h1 class="title">
    <span class="mid">Discover Reef</span><br>
    Lumen Tide Dive
  </h1>
  <p class="intro">You want to learn more about our reef?<br>Participate in our Discover Lumen Tide Dive!<br>In half a day we show you what we do to help our reef.</p>
  <div class="photo photo-main" role="img" aria-label="Underwater photo of a diver above staghorn coral on a Bonaire reef">
    <svg class="photo-edge" viewBox="0 0 470 70" preserveAspectRatio="none" aria-hidden="true">
      <path d="M0 0H470V30C445 46 420 24 392 38C362 54 334 30 304 42C274 56 246 34 216 46C186 58 158 36 128 48C98 60 70 40 42 52C26 58 12 52 0 46Z" fill="var(--paper)"/>
    </svg>
  </div>
  <div class="photo-pair">
    <div class="shallows" role="img" aria-label="Photo of corals in clear shallow water"></div>
    <div class="field" role="img" aria-label="Photo of a wide field of staghorn coral"></div>
  </div>
  <div class="social"><span class="social-mark"></span><span class="social-mark"></span>kqdivebonaire</div>
</article>

</body>
</html>
```